Design Business Card Aerial Drone Photography

we need a business card that shows we are a leader in:
-Aerial Videos
-Aerial Photography
-Aerial Real Estate Photography
the attached logo is in blue, however please feel free to submit creative colors and designs
Updates

I would like to add the words "Veteran Owned and Operated" to my business card Certified Drone Operator should appear as one line Thanks, Ned Corliss

Target Market(s)

real estate, cell towers, companies that want to showcase their company with aerial drone photography

Contact Information for Business Card

logo files have been submitted in pdf, jpg, png, .ai, .eps., .svg formats. Please feel free to be creative with design and colors, possibly a cloud type background
sample attached.
review my website www.brightwrenaerial.example that should help with designing my business card
Services:
-Aerial Videos
-Aerial Photography

Font styles to use
Sans Serif

Colors

Designer to choose colors to be used in the design.

Requirements
Must have
• company logo
• Bright Wren Aerial
• Ned Corliss Certified Drone Operator
• 555-619-4827
• brightwrenaerial@mailbox.example
• www.brightwrenaeriel.example
• 2971 Maplewood Ln, Dunwoody GA 30338
Nice to have
• Please feel free to be creative with design and colors

```html
<!DOCTYPE html>
<html lang="en">
<head>
<meta charset="utf-8">
<title>Bright Wren Aerial — Business Card</title>
<link href="https://fonts.googleapis.com/css2?family=Lato:wght@400;700;900&display=swap" rel="stylesheet">
<style>
  :root {
    --stage: #2a2a2a;
    --card-dark: #161616;
    --card-light: #ffffff;
    --brand-blue: #1a7fd4;
    --text-light: #f2f2f2;
    --rule: #9a9a9a;
  }
  * { box-sizing: border-box; margin: 0; padding: 0; }
  html, body { width: 1200px; height: 900px; overflow: hidden; }
  body {
    background: var(--stage);
    font-family: "Lato", Arial, sans-serif;
    position: relative;
  }
  .card {
    position: absolute;
    width: 640px;
    height: 366px;
    border-radius: 18px;
    overflow: hidden;
    box-shadow: 0 18px 40px rgba(0,0,0,.45);
  }

  /* Back side */
  .card-back { left: 60px; top: 50px; background: var(--card-dark); }
  .card-back .brand-name {
    position: absolute; left: 0; right: 0; top: 120px;
    text-align: center;
    color: var(--brand-blue);
    font-weight: 900; font-size: 44px; letter-spacing: 1px;
    text-transform: uppercase;
  }
  .card-back .website {
    position: absolute; left: 0; right: 0; top: 236px;
    text-align: center;
    color: var(--brand-blue);
    font-weight: 700; font-size: 14px; letter-spacing: 3px;
  }
  .card-back .divider {
    position: absolute; left: 150px; right: 150px; top: 264px;
    height: 1px; background: var(--rule);
  }
  .card-back .tagline {
    position: absolute; left: 0; right: 0; top: 276px;
    text-align: center;
    color: var(--text-light);
    font-weight: 700; font-size: 13px;
  }

  /* Front side */
  .card-front { left: 500px; top: 480px; background: var(--card-dark); }
  .card-front .panel { position: absolute; inset: 0; width: 640px; height: 366px; }
  .card-front .brand-name {
    position: absolute; left: 392px; top: 52px; width: 228px;
    text-align: center;
    color: var(--brand-blue);
    font-weight: 900; font-size: 26px; letter-spacing: .5px;
    text-transform: uppercase; line-height: 1.1;
  }
  .identity { position: absolute; left: 36px; top: 128px; }
  .identity .person-name {
    color: var(--brand-blue); font-weight: 900; font-size: 17px; text-transform: uppercase;
  }
  .identity .role { color: var(--text-light); font-size: 14px; margin-top: 3px; }
  .identity .credential { color: var(--brand-blue); font-size: 14px; margin-top: 3px; }

  .contacts { position: absolute; left: 36px; top: 214px; list-style: none; }
  .contacts li {
    display: flex; align-items: center; gap: 10px;
    color: var(--text-light); font-size: 13px; margin-bottom: 6px;
  }
  .contacts .address { color: var(--brand-blue); font-weight: 700; }
  .contacts svg { width: 14px; height: 14px; flex: none; }
  .contacts .address .spacer { width: 14px; }

  .services { position: absolute; left: 36px; top: 298px; }
  .services h3 {
    color: var(--brand-blue); font-weight: 700; font-size: 13px; text-transform: uppercase;
  }
  .services ul { list-style: none; margin-top: 3px; }
  .services li {
    color: var(--text-light); font-weight: 700; font-size: 12px; text-transform: uppercase;
    display: flex; align-items: center; gap: 7px; line-height: 1.35;
  }
  .services li::before {
    content: ""; width: 5px; height: 5px; border-radius: 50%; background: var(--brand-blue);
  }
  .services-rule {
    position: absolute; left: 190px; top: 290px; width: 330px; height: 1px;
    background: linear-gradient(90deg, var(--rule), transparent);
  }
</style>
</head>
<body>

  <section class="card card-back" aria-label="Card back">
    <div class="brand-name">Bright Wren Aerial</div>
    <div class="website">www.brightwrenaerial.example</div>
    <div class="divider"></div>
    <p class="tagline">For Film, Sports Events, Weddings, Agriculture, Business and More...</p>
  </section>

  <section class="card card-front" aria-label="Card front">
    <svg class="panel" viewBox="0 0 640 366" preserveAspectRatio="none" aria-hidden="true">
      <polygon points="200,0 640,0 640,300" fill="var(--card-light)"/>
      <g stroke="var(--card-light)" stroke-width="3">
        <line x1="188" y1="0" x2="640" y2="308"/>
        <line x1="180" y1="0" x2="640" y2="313"/>
        <line x1="172" y1="0" x2="640" y2="319"/>
      </g>
    </svg>

    <div class="brand-name">Bright Wren<br>Aerial</div>

    <div class="identity">
      <div class="person-name">Ned Corliss</div>
      <div class="role">Certified Drone Operator</div>
      <div class="credential">Veteran Owned &amp; Operated</div>
    </div>

    <ul class="contacts">
      <li>
        <svg viewBox="0 0 24 24" aria-hidden="true"><path fill="#f2f2f2" d="M6.6 10.8a15.1 15.1 0 0 0 6.6 6.6l2.2-2.2a1 1 0 0 1 1-.25 11.4 11.4 0 0 0 3.6.57 1 1 0 0 1 1 1V20a1 1 0 0 1-1 1A17 17 0 0 1 3 4a1 1 0 0 1 1-1h3.5a1 1 0 0 1 1 1c0 1.25.2 2.450.57 3.57a1 1 0 0 1-.25 1z"/></svg>
        555-619-4827
      </li>
      <li>
        <svg viewBox="0 0 24 24" aria-hidden="true"><rect x="2" y="5" width="20" height="14" rx="1" fill="#f2f2f2"/><path d="M3 6l9 7 9-7" fill="none" stroke="#161616" stroke-width="1.6"/></svg>
        brightwrenaerial@mailbox.example
      </li>
      <li class="address"><span class="spacer"></span>2971 Maplewood Ln, Dunwoody GA 30338</li>
    </ul>

    <div class="services-rule"></div>
    <div class="services">
      <h3>Our Services:</h3>
      <ul>
        <li>Aerial Videos &amp; Photography</li>
        <li>Aerial Real Estate Photography</li>
      </ul>
    </div>
  </section>

</body>
</html>
```